Bright Towns Alliance PowerPoint Design Template and Sample Deck

The Bright Towns Alliance is an international organization that seeks to improve the livability, workability and sustainability of the world’s cities.
We seek a versatile PowerPoint design template with 10 slide types plus a “self-documenting” sample deck. Your design will be used in keynote speeches and workshops around the world.
After the contest is completed, we will ask the winning designer to add 10-20 additional slide types for $75 per slide. We also seek a long-term relationship whereby we can request “custom” slides and/or ask the designer to touch up the slides we build to make them better.
FILES. We have uploaded several files:
1. BRIGHT TOWNS ALLIANCE DESIGN CONTEST NOTES.docx with full instructions.
2. PALETTE. Shows our official colors.
3 LOGOS. Several individual files with different variations of our logo. Some with our motto, some without.
2. SAMPLE SLIDES. Because we were unable to successfully upload our sample deck, we are making it available via this FileCrate link:
https://www.filecrate-example.net/s/k7qvmr2tn8wzd4h/The%20Bright%20Towns%20Alliance%20Design%20Contest%20Notes.docx?dl=0
Target Market(s)
Mayors, department heads, CIOs, senior executives from technology companies
Industry/Entity Type
Information Technology
Colors
Designer to choose colors to be used in the design.
Requirements
Must have
- Please see uploaded Word document for requirements, nice to haves and should not haves and uploaded palette for color preferences.
Nice to have
- see above
Should not have
- see above

```html
<!DOCTYPE html>
<html lang="en">
<head>
<meta charset="utf-8">
<title>Bright Towns Alliance – Slide Template</title>
<link rel="stylesheet" href="https://fonts.googleapis.com/css2?family=Carlito:ital,wght@0,400;0,700;1,400&family=Arimo:ital,wght@0,400;0,700;1,400&display=swap">
<style>
  :root{
    --stage:#626262;
    --navy:#032a57;
    --orange:#f18f2b;
    --white:#ffffff;
    --ink:#1c2b45;
    --map-grey:#d9d9d9;
    --arrow-grey:#7a7a7a;
    --label-grey:#6f6f6f;
    --row-a:#c9cfe6;
    --row-b:#e3e6f2;
    --line:#c98a3c;
  }
  *{box-sizing:border-box;margin:0;padding:0}
  html,body{width:1200px;height:960px;overflow:hidden;background:var(--stage)}
  body{position:relative;font-family:"Carlito",Calibri,sans-serif;color:var(--white)}
  .slide{position:absolute;width:480px;height:270px;overflow:hidden}
  .slide--navy{background:var(--navy)}
  .slide--white{background:var(--white)}
  .abs{position:absolute}

  .page-mark{position:absolute;left:50%;bottom:0;transform:translateX(-50%);width:34px;height:16px}
  .page-mark svg{display:block}
  .page-mark span{position:absolute;left:0;right:0;bottom:2px;text-align:center;font-size:5.5px;color:var(--ink)}

  /* world maps */
  .brand-box{left:24px;top:1px;width:56px;height:48px;background:var(--white);color:var(--navy);font-size:11.5px;line-height:12px;padding:4px 3px}
  .section-title{color:var(--orange);text-decoration:underline;text-underline-offset:3px;text-decoration-thickness:1.5px;font-weight:400}
  .map-title{left:24px;top:92px;font-size:19px;line-height:23px;font-weight:700;letter-spacing:.5px}
  .map-copy{left:26px;top:146px;width:100px;font-size:5.6px;line-height:10.8px;text-align:justify}
  .map-area{left:140px;top:38px;width:330px;height:194px;background:radial-gradient(ellipse at 50% 45%,#e2e2e2 0%,#d6d9de 65%,var(--navy) 100%);border-radius:40px}
  .pin{font-family:"Arimo",Arial,sans-serif;font-size:5px;font-weight:700;letter-spacing:.6px;text-align:center;color:var(--white)}
  .pin b{display:block;padding:2px 4px;line-height:6px}
  .pin i{display:block;width:0;height:0;margin:0 auto;border-left:4px solid transparent;border-right:4px solid transparent}
  .pin--grey b{background:var(--label-grey)}
  .pin--grey i{border-top:7px solid var(--label-grey)}
  .pin--orange b{background:var(--orange)}
  .pin--orange i{border-top:7px solid var(--orange)}

  /* table */
  .table-band{left:0;top:23px;width:480px;height:47px;background:var(--navy);text-align:center}
  .table-band h2{font-size:18px;color:var(--orange);text-decoration:underline;text-decoration-thickness:1px;text-underline-offset:2px;padding-top:11px;line-height:20px}
  .table-band p,.process-sub{font-size:4.6px;font-style:italic;color:var(--white)}
  .data-table{border-collapse:collapse;width:208px;font-family:"Arimo",Arial,sans-serif}
  .data-table th{background:var(--navy);color:var(--orange);font-family:"Carlito",sans-serif;font-size:8px;font-weight:700;text-align:left;padding:2px 3px;height:17px;border-right:1px solid var(--white)}
  .data-table td{font-size:4.3px;line-height:8.5px;color:#333;padding:1px 6px;height:19px;vertical-align:top;border-right:1px solid var(--white);border-bottom:1px solid var(--white)}
  .data-table tr:nth-child(odd) td{background:var(--row-a)}
  .data-table tr:nth-child(even) td{background:var(--row-b)}

  /* image + text */
  .wordmark{right:6px;top:18px;font-family:"Arimo",Arial,sans-serif;font-size:28px;color:var(--navy);letter-spacing:-1px}
  .photo{background:linear-gradient(170deg,#0d2a5e 0%,#2c5da8 40%,#c98a4a 75%,#16224a 100%)}
  .feature h3{font-family:"Arimo",Arial,sans-serif;font-size:6.5px;letter-spacing:1.4px;color:var(--ink);font-weight:700;border-left:1px solid #888;padding-left:6px}
  .feature p{font-family:"Arimo",Arial,sans-serif;font-style:italic;font-size:5.3px;line-height:10.8px;color:var(--ink);padding-left:8px;margin-top:5px;width:96px}

  /* timeline */
  .timeline-title{left:21px;top:42px;font-size:22px;letter-spacing:.3px}
  .rule{height:1px;background:var(--line)}
  .node{width:48px;height:48px;border-radius:50%;background:var(--orange);color:var(--navy);font-size:8px;display:flex;align-items:center;justify-content:center}
  .year{font-size:13px;color:var(--orange)}
  .event{font-size:6.4px;line-height:8.4px;width:80px}

  /* linear process */
  .process-title{left:0;right:0;top:28px;text-align:center;font-size:17px;font-weight:700;color:var(--orange)}
  .process-sub{left:0;right:0;top:57px;text-align:center}
  .process-rule{left:60px;width:360px;height:1px;background:#1f3e69}
  .process-intro{left:130px;width:220px;top:94px;text-align:center;font-size:4.9px;font-style:italic;line-height:9.6px}
  .step h4{font-family:"Arimo",Arial,sans-serif;font-size:4.8px;letter-spacing:1.2px;font-weight:700}
  .step p{font-size:5.3px;line-height:9.8px;margin-top:3px;width:60px}
</style>
</head>
<body>

<!-- Slide 7: world maps -->
<section class="slide slide--navy" style="left:96px;top:41px">
  <div class="abs brand-box">Bright Towns Alliance</div>
  <h2 class="abs section-title map-title">WORLD<br>MAPS</h2>
  <p class="abs map-copy">A company is an association or collection of individuals, whether naturalpianor persons, legal persons, or a mixture of both. Company members share a common purpose and unite in order to focus their various alepue hom haihai hom pokok jih nyan beu</p>
  <div class="abs map-area" role="img" aria-label="World map showing office locations"></div>
  <div class="abs pin pin--grey" style="left:162px;top:86px"><b>AGENCY</b><i></i></div>
  <div class="abs pin pin--orange" style="left:302px;top:93px"><b>HOME<br>OFFICE</b><i></i></div>
  <div class="abs pin pin--grey" style="left:389px;top:61px"><b>AGENCY</b><i></i></div>
  <div class="page-mark"><svg width="34" height="16"><polygon points="17,0 34,16 0,16" fill="var(--orange)"/></svg><span>7</span></div>
</section>

<!-- Slide 8: table -->
<section class="slide slide--white" style="left:628px;top:41px">
  <div class="abs table-band">
    <h2>TABLE</h2>
    <p>Sed ut perspiciatis unde omnis iste natus error sit voluptatem</p>
  </div>
  <table class="abs data-table" style="left:29px;top:91px">
    <tr><th>Info</th><th>Description</th></tr>
    <tr><td>Sed Ut Perspiciatis Unde Omnis Iste Natus Error Sit</td><td>Sed Ut Perspiciatis Unde Omnis Iste Natus Error</td></tr>
    <tr><td>Sed Ut Perspiciatis Unde Omnis Iste Natus Error Sit</td><td>Sed Ut Perspiciatis Unde Omnis Iste Natus Error</td></tr>
    <tr><td>Sed Ut Perspiciatis Unde Omnis Iste Natus Error Sit</td><td>Sed Ut Perspiciatis Unde Omnis Iste Natus Error</td></tr>
    <tr><td>Sed Ut Perspiciatis Unde Omnis Iste Natus Error Sit</td><td>Sed Ut Perspiciatis Unde Omnis Iste Natus Error</td></tr>
    <tr><td>Sed Ut Perspiciatis Unde Omnis Iste Natus Error Sit</td><td>Sed Ut Perspiciatis Unde Omnis Iste Natus Error</td></tr>
    <tr><td>Sed Ut Perspiciatis Unde Omnis Iste Natus Error Sit</td><td>Sed Ut Perspiciatis Unde Omnis Iste Natus Error</td></tr>
    <tr><td>Sed Ut Perspiciatis Unde Omnis Iste Natus Error Sit</td><td>Sed Ut Perspiciatis Unde Omnis Iste Natus Error</td></tr>
  </table>
  <table class="abs data-table" style="left:251px;top:92px">
    <tr><th>Info</th><th>Description</th></tr>
    <tr><td>Sed Ut Perspiciatis Unde Omnis Iste Natus Error Sit</td><td>Sed Ut Perspiciatis Unde Omnis Iste Natus Error</td></tr>
    <tr><td>Sed Ut Perspiciatis Unde Omnis Iste Natus Error Sit</td><td>Sed Ut Perspiciatis Unde Omnis Iste Natus Error</td></tr>
    <tr><td>Sed Ut Perspiciatis Unde Omnis Iste Natus Error Sit</td><td>Sed Ut Perspiciatis Unde Omnis Iste Natus Error</td></tr>
    <tr><td>Sed Ut Perspiciatis Unde Omnis Iste Natus Error Sit</td><td>Sed Ut Perspiciatis Unde Omnis Iste Natus Error</td></tr>
    <tr><td>Sed Ut Perspiciatis Unde Omnis Iste Natus Error Sit</td><td>Sed Ut Perspiciatis Unde Omnis Iste Natus Error</td></tr>
    <tr><td>Sed Ut Perspiciatis Unde Omnis Iste Natus Error Sit</td><td>Sed Ut Perspiciatis Unde Omnis Iste Natus Error</td></tr>
    <tr><td>Sed Ut Perspiciatis Unde Omnis Iste Natus Error Sit</td><td>Sed Ut Perspiciatis Unde Omnis Iste Natus Error</td></tr>
  </table>
  <div class="page-mark"><svg width="34" height="16"><polygon points="17,0 34,16 0,16" fill="var(--orange)"/></svg><span>8</span></div>
</section>

<!-- Slide 9: image and text -->
<section class="slide slide--white" style="left:98px;top:339px">
  <div class="abs wordmark">Bright Towns Alliance</div>
  <div class="abs photo" style="left:58px;top:85px;width:109px;height:144px" role="img" aria-label="City skyline at night with light trails"></div>
  <div class="abs photo" style="left:318px;top:80px;width:109px;height:145px" role="img" aria-label="City skyline at night with light trails"></div>
  <div class="abs feature" style="left:186px;top:84px">
    <h3>TITLE HERE 01</h3>
    <p>A company is an association or collection of individuals, whether naturalpianor persons, legal persons, or a mixture of both.</p>
  </div>
  <div class="abs feature" style="left:186px;top:173px">
    <h3>TITLE HERE 02</h3>
    <p>A company is an association or collection of individuals, whether naturalpianor persons, legal persons, or a mixture of both.</p>
  </div>
  <svg class="abs" style="left:172px;top:122px" width="16" height="12"><polygon points="0,4 9,4 9,0 16,6 9,12 9,8 0,8" fill="var(--navy)"/></svg>
  <svg class="abs" style="left:293px;top:201px" width="16" height="12"><polygon points="16,4 7,4 7,0 0,6 7,12 7,8 16,8" fill="var(--navy)"/></svg>
  <div class="page-mark"><svg width="34" height="16"><polygon points="17,0 34,16 0,16" fill="var(--orange)"/></svg><span>9</span></div>
</section>

<!-- Slide 10: timeline start -->
<section class="slide slide--navy" style="left:628px;top:339px">
  <h2 class="abs section-title timeline-title">TIMELINE</h2>
  <div class="abs rule" style="left:48px;top:174px;width:432px"></div>
  <div class="abs node" style="left:24px;top:150px">BEGIN</div>
  <div class="abs year" style="left:190px;top:104px">2011</div>
  <p class="abs event" style="left:176px;top:127px">Ut velit arcu, interdum sit amet accumsan et, scelerisque sit amet tellus. Aenean nec nisl lacus.</p>
  <div class="abs year" style="left:389px;top:100px">2013</div>
  <p class="abs event" style="left:374px;top:121px">Ut velit arcu, interdum sit amet accumsan et, scelerisque sit amet tellus. Aenean nec nisl lacus.</p>
  <div class="abs year" style="left:99px;top:181px">2010</div>
  <p class="abs event" style="left:82px;top:202px">Ut velit arcu, interdum sit amet accumsan et, scelerisque sit amet tellus. Aenean nec nisl lacus.</p>
  <div class="abs year" style="left:287px;top:184px">2012</div>
  <p class="abs event" style="left:276px;top:208px">Ut velit arcu, interdum sit amet accumsan et, scelerisque sit amet tellus. Aenean nec nisl lacus.</p>
</section>

<!-- Slide 11: timeline end -->
<section class="slide slide--navy" style="left:98px;top:648px">
  <div class="abs rule" style="left:0;top:138px;width:432px"></div>
  <div class="abs node" style="left:407px;top:114px">END</div>
  <div class="abs year" style="left:129px;top:60px">2014</div>
  <p class="abs event" style="left:116px;top:90px">Ut velit arcu, interdum sit amet accumsan et, scelerisque sit amet tellus. Aenean nec nisl lacus.</p>
  <div class="abs year" style="left:326px;top:58px">2016</div>
  <p class="abs event" style="left:315px;top:85px">Ut velit arcu, interdum sit amet accumsan et, scelerisque sit amet tellus. Aenean nec nisl lacus.</p>
  <div class="abs year" style="left:39px;top:144px">2013</div>
  <p class="abs event" style="left:22px;top:165px">Ut velit arcu, interdum sit amet accumsan et, scelerisque sit amet tellus. Aenean nec nisl lacus.</p>
  <div class="abs year" style="left:227px;top:147px">2015</div>
  <p class="abs event" style="left:216px;top:170px">Ut velit arcu, interdum sit amet accumsan et, scelerisque sit amet tellus. Aenean nec nisl lacus.</p>
</section>

<!-- Slide 12: linear process -->
<section class="slide slide--navy" style="left:624px;top:648px">
  <h2 class="abs process-title">LINEAR PROCESS</h2>
  <p class="abs process-sub">Sed ut perspiciatis unde omnis iste natus error sit voluptatem</p>
  <div class="abs process-rule" style="top:90px"></div>
  <p class="abs process-intro">A company is an association or collection of individuals, whether naturalpianor persons, legal persons, or a mixture of both.mpany members share a common purpose an</p>
  <div class="abs process-rule" style="top:122px"></div>
  <svg class="abs" style="left:80px;top:138px" width="320" height="44">
    <polygon points="0,22 24,0 24,9 68,9 68,35 24,35 24,44" fill="var(--arrow-grey)"/>
    <polygon points="82,22 106,0 106,9 150,9 150,35 106,35 106,44" fill="var(--arrow-grey)"/>
    <polygon points="237,22 213,0 213,9 168,9 168,35 213,35 213,44" fill="var(--orange)"/>
    <polygon points="318,22 294,0 294,9 250,9 250,35 294,35 294,44" fill="var(--arrow-grey)"/>
  </svg>
  <div class="abs step" style="left:90px;top:203px"><h4>TITLE HERE</h4><p>Lorem ipsum dolor sit amet aleh pue hom hai nyang penting olah dan</p></div>
  <div class="abs step" style="left:171px;top:204px"><h4>TITLE HERE</h4><p>Lorem ipsum dolor sit amet aleh pue hom hai nyang penting olah dan</p></div>
  <div class="abs step" style="left:250px;top:205px"><h4>TITLE HERE</h4><p>Lorem ipsum dolor sit amet aleh pue hom hai nyang penting olah dan</p></div>
  <div class="abs step" style="left:330px;top:203px"><h4>TITLE HERE</h4><p>Lorem ipsum dolor sit amet aleh pue hom hai nyang penting olah dan</p></div>
  <div class="page-mark"><svg width="34" height="16"><polygon points="17,0 34,16 0,16" fill="var(--orange)"/></svg><span>12</span></div>
</section>

</body>
</html>
```